Brightfern World Learning is to provide global summer programs in the United States through which students from the US and China share experiences, intensive learning, and each other’s cultures. The program seeks to more fully prepare both the US and Chinese students for their college education and future careers in this interdependent world. Chinese students are individually paired with US Students where they will reside US students' home for the period of the program.

Current website: Brightfern World Learning

Need to support both English and Chinese with different font.

Project Deadline Extended
Reason: Because of Thanksgiving Holidays.

Dear Designers,

In order to generate the best design, I uploaded some photos from our global summer program. Please check:

http://brightfernworldlearning.org/photos/

Colette

My company Logo just added to the project.

Sorry for the late update.

Project Deadline Extended
Reason: Due to Thanksgiving holiday, I don't have enough time to provide feedback to all the designers. Colette

Project Deadline Extended
Reason: Holiday season. Need more time for designer and myself.

Target Market(s)

Grade K to 12 students and their parents to sign up the global summer program. Majority audience are from China.

Industry/Entity Type

College

Font styles to use
Sans Serif

Colors
3277b5

Requirements
Must have
• You may check my current website for the summer program content
www.brightfernworldlearning.org
Check these two clips to see what service we provided.
http://www.vidhaven.example/watch?v=7kR3nq41xTm&feature=vh.be
https://www.vidhaven.example/watch?v=W8d2JP6h4oZ

Company Logo are included in the attachment.

Some photos from summer program: http://brightfernworldlearning.org/photos/
The website should show the students one to one relationship.
The website should show homestay part.

I want Photo Slider on each page to share the fun activities.

Each program will be provide a video clip as a summery.

The website should support font of both English and Chinese. I like to see both Chinese and English on the same page instead of switch back and forth. I can add Chinese part later if you leave the room.

Nice to have
• I have a lot of paired pictures. I am wondering if I can use collage of photos as the background.

The design should be playful and fun!

```html
<!DOCTYPE html>
<html lang="en">
<head>
<meta charset="utf-8">
<title>Brightfern World Learning</title>
<link rel="stylesheet" href="https://fonts.googleapis.com/css2?family=Montserrat:wght@500;600&family=Noto+Sans+SC:wght@400;500&family=Noto+Serif:ital,wght@0,400;1,400&family=Open+Sans:wght@400;600&display=swap">
<style>
  :root {
    --navy: #1d3263;
    --blue: #3277b5;
    --gold: #f0b51e;
    --gold-dark: #d99d10;
    --white: #ffffff;
    --text: #6d6d6d;
    --chip: #c9d3e6;
    --rule: #d9dde6;
  }
  * { box-sizing: border-box; margin: 0; padding: 0; }
  html, body { width: 1200px; height: 1000px; overflow: hidden; background: var(--white); }
  body { font-family: "Open Sans", Arial, sans-serif; color: var(--text); position: relative; }
  .zh { font-family: "Noto Sans SC", "Open Sans", sans-serif; }

  .top-bar {
    height: 38px; background: var(--navy);
    display: flex; align-items: center; justify-content: space-between;
    padding: 0 272px 0 165px;
  }
  .social { display: flex; gap: 6px; align-items: center; }
  .social .search { width: 16px; height: 16px; }
  .social .chip { width: 16px; height: 16px; background: var(--chip); border-radius: 2px; }
  .top-bar .call { font-size: 10px; color: #b8c3da; white-space: nowrap; }

  .site-header {
    height: 72px; display: flex; align-items: center; justify-content: center; gap: 12px;
    border-bottom: 1px solid var(--rule);
  }
  .brand-mark { width: 34px; height: 34px; border-radius: 50%; background: var(--gold); }
  .brand-name {
    font-family: "Montserrat", Arial, sans-serif; font-weight: 600;
    font-size: 24px; letter-spacing: 2.5px; color: var(--blue); text-transform: uppercase;
  }
  .brand-bar { width: 3px; height: 32px; background: var(--gold); margin-left: 6px; }

  .student-login {
    position: absolute; top: 2px; left: 950px; width: 76px; height: 122px;
    background: var(--gold); z-index: 2;
    display: flex; flex-direction: column; align-items: center; justify-content: space-between;
    padding: 6px 0 10px; color: var(--white);
    font-weight: 600; font-size: 9px; text-transform: uppercase; text-align: center; line-height: 1.15;
    border-bottom: 3px solid var(--gold-dark);
  }
  .student-login .seal { width: 46px; height: 46px; border-radius: 50%; border: 2px solid var(--white); }

  .main-nav {
    height: 42px; background: var(--navy); border-bottom: 4px solid var(--gold);
    display: flex; padding-left: 320px;
  }
  .main-nav a {
    font-family: "Noto Serif", Georgia, serif; font-size: 13px; text-transform: uppercase;
    color: var(--white); text-decoration: none; padding: 0 14px;
    display: flex; align-items: center; gap: 8px;
  }
  .main-nav a.active { background: var(--gold); }
  .main-nav .caret { width: 0; height: 0; border-left: 4px solid transparent; border-right: 4px solid transparent; border-top: 4px solid var(--gold); }
  .main-nav a.active .caret { border-top-color: var(--white); }

  .hero {
    margin: 26px auto 0; width: 900px; height: 280px;
    background: linear-gradient(135deg, #5a67c2 0%, #3f4fb0 45%, #6c79cc 100%);
    box-shadow: 0 10px 14px -8px rgba(0,0,0,.45);
  }

  .promo {
    margin: 30px auto 0; width: 890px; height: 56px; background: var(--navy);
    border-left: 4px solid var(--gold);
    display: flex; align-items: center; justify-content: space-between; padding: 0 18px;
  }
  .promo p { font-family: "Noto Serif", Georgia, serif; font-style: italic; font-size: 18px; color: var(--white); white-space: nowrap; }
  .promo p em { color: var(--gold); }
  .promo .button {
    background: var(--gold); color: var(--white); font-size: 11px; padding: 6px 12px;
    border-radius: 2px; text-decoration: none; white-space: nowrap;
  }

  .features {
    width: 900px; margin: 22px auto 0; display: grid; grid-template-columns: repeat(4, 1fr); gap: 26px;
  }
  .feature-head { display: flex; align-items: center; gap: 12px; margin-bottom: 16px; }
  .feature-head svg { width: 38px; height: 38px; flex: none; }
  .feature-head h2 { font-family: "Noto Serif", Georgia, serif; font-weight: 400; font-size: 19px; color: var(--navy); white-space: nowrap; }
  .feature p { font-size: 11px; line-height: 1.7; color: var(--text); }
  .feature .more { display: block; margin-top: 4px; font-size: 11px; color: var(--gold); text-decoration: none; }

  .tabs { width: 900px; margin: 30px auto 0; display: flex; gap: 3px; }
  .tabs a {
    font-family: "Noto Serif", Georgia, serif; font-size: 14px; color: var(--white);
    background: var(--navy); padding: 10px 12px 8px; text-decoration: none; white-space: nowrap;
  }
  .tabs a.active { background: var(--gold); }
  .tab-panel {
    width: 900px; margin: 0 auto; height: 140px; background: var(--navy);
    border-top: 4px solid var(--gold); display: grid; grid-template-columns: repeat(3, 1fr); gap: 20px; padding: 12px 14px;
  }
  .tab-panel .photo { background: linear-gradient(180deg, #8f9bd6, #4d5bb6); }
  .tab-panel .photo.light { background: linear-gradient(180deg, #f4f5f8, #c7cde0); }
  .tab-panel .photo.warm { background: linear-gradient(180deg, #7a6a5c, #3e3630); }
</style>
</head>
<body>
  <div class="top-bar">
    <div class="social">
      <svg class="search" viewBox="0 0 16 16"><circle cx="6.5" cy="6.5" r="4" fill="none" stroke="#c9d3e6" stroke-width="1.6"/><line x1="9.5" y1="9.5" x2="13.5" y2="13.5" stroke="#c9d3e6" stroke-width="1.8"/></svg>
      <span class="chip"></span><span class="chip"></span><span class="chip"></span><span class="chip"></span><span class="chip"></span><span class="chip"></span>
    </div>
    <span class="call">Call us today! 555-013-4872</span>
  </div>

  <header class="site-header">
    <span class="brand-mark"></span>
    <span class="brand-name">Brightfern World Learning</span>
    <span class="brand-bar"></span>
  </header>

  <a class="student-login"><span>Current</span><span class="seal"></span><span>Student<br>Login</span></a>

  <nav class="main-nav">
    <a class="active">Home <span class="caret"></span></a>
    <a>Features <span class="caret"></span></a>
    <a>Campus Life <span class="caret"></span></a>
    <a>News &amp; Events <span class="caret"></span></a>
    <a>Contact Us</a>
  </nav>

  <div class="hero" role="img" aria-label="Blue-toned collage of paired US and Chinese student photos from the summer program"></div>

  <div class="promo">
    <p>Summer 2015 with <em>Brightfern Homestay Exchange</em>, our One-to-One Pairing Program.</p>
    <a class="button">Apply Now</a>
  </div>

  <section class="features">
    <div class="feature">
      <div class="feature-head">
        <svg viewBox="0 0 38 38"><rect x="6" y="26" width="26" height="6" fill="#1d3263"/><rect x="8" y="19" width="22" height="6" fill="#1d3263"/><circle cx="19" cy="11" r="6" fill="#1d3263"/><rect x="18.5" y="2" width="2" height="4" fill="#1d3263"/></svg>
        <h2>Campus Life</h2>
      </div>
      <p>Each Chinese student is paired one to one with a US student and lives in the partner’s family home. <span class="zh" lang="zh">一对一配对，寄宿美国家庭。</span></p>
      <a class="more">| Read More</a>
    </div>
    <div class="feature">
      <div class="feature-head">
        <svg viewBox="0 0 38 38"><circle cx="19" cy="19" r="18" fill="#1d3263"/><text x="19" y="26" text-anchor="middle" font-family="Noto Serif, serif" font-size="22" fill="#fff">π</text></svg>
        <h2>Admissions</h2>
      </div>
      <p>Grade K to 12 students and parents can sign up for our global summer program and host family stays here. <span class="zh" lang="zh">欢迎家长为孩子报名。</span></p>
      <a class="more">| Read More</a>
    </div>
    <div class="feature">
      <div class="feature-head">
        <svg viewBox="0 0 38 38"><path d="M4 34 L4 4 L34 34 Z" fill="#1d3263"/><path d="M11 27 L11 20 L18 27 Z" fill="#fff"/><line x1="6" y1="20" x2="30" y2="4" stroke="#1d3263" stroke-width="3"/></svg>
        <h2>Athletics</h2>
      </div>
      <p>Paired students learn, play and compete side by side, on the field and the court, building friendship for life. <span class="zh" lang="zh">一起运动，结下友谊。</span></p>
      <a class="more">| Read More</a>
    </div>
    <div class="feature">
      <div class="feature-head">
        <svg viewBox="0 0 38 38"><rect x="7" y="3" width="24" height="32" rx="2" fill="#1d3263"/><rect x="11" y="3" width="2" height="32" fill="#fff"/></svg>
        <h2>News &amp; Events</h2>
      </div>
      <p>Watch each program’s video summary and see photos of the fun activities our students share every summer. <span class="zh" lang="zh">精彩活动视频与照片。</span></p>
      <a class="more">| Read More</a>
    </div>
  </section>

  <nav class="tabs">
    <a class="active">Our Mission</a>
    <a>Future Students</a>
    <a>Living With A Host Family</a>
    <a>Paired Students</a>
    <a>Program Videos</a>
    <a>Photo Gallery</a>
  </nav>
  <div class="tab-panel">
    <div class="photo light" role="img" aria-label="Program activity photo"></div>
    <div class="photo" role="img" aria-label="Paired students on a group outing"></div>
    <div class="photo warm" role="img" aria-label="Homestay family activity photo"></div>
  </div>
</body>
</html>
```